Design a WordPress layout for a home loans company

The home loans company in question is going through a rebrand and needs a new website layout.
Sites they like: http://www.brightnestlending.com.au/
Current logo: Attached.
Colours to be used: As per those used in logo.
Primary: #71aa3d
Secondary: #130e10
Pages to be designed:
- Homepage
- Internal services page
Menu items for display purposes:
- Home
- About Us
- Speak to a Broker
- Articles
- Contact Us
A modern design with simplicity is key.
For copy, dummy text such as Lorem ipsum will be fine.
If you would like anything elso, please ask.
Target Market(s)
25-40 year old
Mostly female
Buying their first home in most cases
Industry/Entity Type
Mortgage Brokerage
Number of Pages Required
2 page
Colors
Designer to choose colors to be used in the design.
Look and feel

```html
<!DOCTYPE html>
<html lang="en">
<head>
<meta charset="utf-8">
<title>Larchway Home Loans</title>
<link rel="stylesheet" href="https://fonts.googleapis.com/css2?family=Open+Sans:wdth,wght@75..100,300..800&display=swap">
<style>
  :root {
    --green: #65c81e;
    --ink: #131313;
    --panel: #c5cbc9;
    --white: #ffffff;
    --text: #1a1a1a;
    --placeholder: #b8b8b8;
  }
  * { box-sizing: border-box; margin: 0; padding: 0; }
  html, body { width: 1200px; height: 3502px; overflow: hidden; }
  body {
    position: relative;
    background: var(--white);
    font-family: "Open Sans", sans-serif;
    font-stretch: 75%;
    color: var(--text);
  }
  .abs { position: absolute; }

  /* Header */
  .brand { left: 62px; top: 38px; display: flex; align-items: center; gap: 14px; }
  .brand__mark { width: 26px; height: 26px; background: var(--green); }
  .brand__name { font-size: 46px; font-weight: 700; color: var(--green); line-height: 1; letter-spacing: -0.5px; }
  .search { left: 822px; top: 9px; width: 252px; height: 42px; border: 3px solid var(--green); }
  .search-icon { left: 1090px; top: 8px; width: 52px; height: 46px; }
  .nav { right: 28px; top: 74px; display: flex; list-style: none; }
  .nav li { font-size: 28px; line-height: 44px; padding: 0 14px; border-left: 5px solid var(--ink); text-transform: uppercase; }
  .nav li:first-child { border-left: none; }
  .nav li.is-active { font-weight: 700; }
  .header-rule { left: 0; top: 140px; width: 1200px; height: 9px; background: var(--green); }

  /* Hero */
  .hero { left: 0; top: 149px; width: 1200px; height: 547px;
    background: linear-gradient(180deg, #8fc3ea 0%, #cfe3ef 34%, #e4e1d8 42%, #d8d2c4 60%, #6fa43c 72%, #5f9a2e 100%); }
  .hero__cta { left: 710px; top: 586px; width: 490px; height: 65px; background: var(--ink); color: var(--green);
    font-size: 37px; font-weight: 600; line-height: 65px; padding-left: 12px; }

  /* Intro */
  .intro__title { left: 47px; top: 772px; font-size: 47px; font-weight: 700; color: var(--green); }
  .intro__text { left: 47px; top: 852px; width: 1106px; font-size: 26px; line-height: 34px; }

  /* Features */
  .feature { top: 1050px; display: flex; }
  .feature__icon { width: 46px; height: 70px; }
  .feature__text { width: 236px; margin-left: 36px; font-size: 25px; line-height: 34px; text-align: justify; }

  /* Quick form */
  .field { border: 3px solid var(--green); background: var(--white); font-size: 13px; color: var(--placeholder);
    padding-left: 10px; display: flex; align-items: center; }
  .btn { background: var(--ink); color: var(--green); font-size: 24px; font-weight: 600; display: flex; align-items: center; padding-left: 22px; }

  /* Cards */
  .card__photo { position: absolute; }
  .photo--house { background: linear-gradient(180deg, #a4c4dc 0%, #cdd8c6 35%, #8a6a4c 55%, #5c9a3c 75%, #8a8f88 100%); }
  .photo--lounge { background: linear-gradient(135deg, #3a2a26 0%, #6a4f44 40%, #c9b9a8 62%, #6c4a34 100%); }
  .photo--sofa { background: linear-gradient(180deg, #2d241c 0%, #6c8a3c 30%, #4a3a2c 55%, #8a8174 100%); }
  .photo--street { background: linear-gradient(180deg, #6a9ac8 0%, #a3a8ac 40%, #8f9598 62%, #4f7a33 82%, #7a5a44 100%); }
  .card__tag { position: absolute; height: 40px; font-size: 25px; line-height: 40px; text-align: right; padding-right: 14px; }
  .tag--dark { background: var(--ink); color: var(--green); }
  .tag--green { background: var(--green); color: var(--ink); text-align: left; padding-left: 18px; }
  .card__text { position: absolute; width: 500px; font-size: 26px; line-height: 34px; text-align: justify; }
  .card__link { position: absolute; font-size: 26px; color: var(--green); display: flex; align-items: center; gap: 12px; }

  /* Contact */
  .contact { left: 84px; top: 2561px; width: 1053px; height: 633px; background: var(--panel); }
  .contact__title { left: 126px; top: 2604px; font-size: 28px; }
  .textarea { left: 126px; top: 2846px; width: 724px; height: 182px; border: 3px solid var(--green); background: var(--white); }

  /* Footer */
  .footer { left: 0; top: 3269px; width: 1200px; height: 233px; background: var(--ink); }
  .footer__social { right: 22px; top: 3280px; font-size: 28px; color: #e6e6e6; }
  .footer__text { left: 233px; top: 3338px; width: 700px; font-size: 26px; line-height: 34px; color: var(--green); }
</style>
</head>
<body>

<header>
  <div class="abs brand"><span class="brand__mark"></span><span class="brand__name">Larchway Home Loans</span></div>
  <div class="abs search"></div>
  <svg class="abs search-icon" viewBox="0 0 52 46" aria-label="Search">
    <circle cx="20" cy="19" r="14" fill="none" stroke="#65c81e" stroke-width="7"/>
    <line x1="30" y1="29" x2="46" y2="42" stroke="#65c81e" stroke-width="9" stroke-linecap="round"/>
  </svg>
  <ul class="abs nav">
    <li>Home</li><li>About Us</li><li>Speak to a Broker</li><li>Articles</li><li class="is-active">Contact Us</li>
  </ul>
  <div class="abs header-rule"></div>
</header>

<section>
  <div class="abs hero" role="img" aria-label="Photo of a single-storey family home with a green front lawn and a for-sale sign"></div>
  <div class="abs hero__cta">Found out more</div>
</section>

<section>
  <h1 class="abs intro__title">LOREM IPSUM</h1>
  <p class="abs intro__text">Lorem ipsum dolor sit amet, consectetur adipiscing elit. Quisque vel metus nec massa efficitur pulvinar. Integer rutrum diam quis lectus accumsan, quis consequat neque faucibus. Morbi tempor bibendum cursus. Duis iaculis sed libero ut consequat. Nam fringilla sed leo pharetra convallis. Sed eu faucibus massa.</p>
</section>

<section>
  <div class="abs feature" style="left:90px">
    <svg class="feature__icon" viewBox="0 0 46 70" aria-label="Dollar"><text x="23" y="58" text-anchor="middle" font-family="Open Sans, sans-serif" font-weight="800" font-size="68" fill="#65c81e">$</text></svg>
    <p class="feature__text">Lorem ipsum dolor sit amet, consectetur adipiscing elit. Quisque vel metus nec massa efficitur pulvinar.</p>
  </div>
  <div class="abs feature" style="left:450px">
    <svg class="feature__icon" viewBox="0 0 46 70" aria-label="Person"><circle cx="23" cy="23" r="22" fill="#65c81e"/><circle cx="23" cy="17" r="8" fill="#fff"/><path d="M9 36 q14 -14 28 0 v2 h-28z" fill="#fff"/></svg>
    <p class="feature__text">Lorem ipsum dolor sit amet, consectetur adipiscing elit. Quisque vel metus nec massa efficitur pulvinar.</p>
  </div>
  <div class="abs feature" style="left:800px">
    <svg class="feature__icon" viewBox="0 0 46 70" aria-label="Location pin"><path d="M23 2 C10 2 3 11 3 21 C3 36 23 62 23 62 C23 62 43 36 43 21 C43 11 36 2 23 2Z" fill="#65c81e"/><circle cx="23" cy="21" r="8" fill="#fff"/></svg>
    <p class="feature__text">Lorem ipsum dolor sit amet, consectetur adipiscing elit. Quisque vel metus nec massa efficitur pulvinar.</p>
  </div>
</section>

<form>
  <div class="abs field" style="left:79px;top:1305px;width:362px;height:47px">lorem ipsum</div>
  <div class="abs field" style="left:458px;top:1305px;width:371px;height:47px">lorem ipsum</div>
  <div class="abs btn" style="left:843px;top:1305px;width:275px;height:47px">Lorem ipsum</div>
</form>

<section>
  <div class="card__photo photo--house" style="left:86px;top:1476px;width:500px;height:317px" role="img" aria-label="Photo of a brick family home with a manicured lawn"></div>
  <div class="card__tag tag--dark" style="left:86px;top:1700px;width:313px">Lorem ipsum</div>
  <p class="card__text" style="left:90px;top:1798px">Lorem ipsum dolor sit amet, consectetur adipiscing elit. Quisque vel metus nec massa efficitur pulvinar. Integer rutrum diam quis lectus accumsan.</p>
  <div class="card__link" style="left:93px;top:1912px">Lorem ipsum <svg width="22" height="28" viewBox="0 0 22 28"><path d="M4 3 L16 14 L4 25" fill="none" stroke="#65c81e" stroke-width="7"/></svg></div>

  <div class="card__photo photo--lounge" style="left:640px;top:1476px;width:490px;height:317px" role="img" aria-label="Photo of a modern living room with white sofas"></div>
  <div class="card__tag tag--green" style="left:808px;top:1693px;width:320px">Lorem ipsum</div>
  <p class="card__text" style="left:638px;top:1798px">Lorem ipsum dolor sit amet, consectetur adipiscing elit. Quisque vel metus nec massa efficitur pulvinar. Integer rutrum diam quis lectus accumsan.</p>
  <div class="card__link" style="left:633px;top:1912px">Lorem ipsum <svg width="22" height="28" viewBox="0 0 22 28"><path d="M4 3 L16 14 L4 25" fill="none" stroke="#65c81e" stroke-width="7"/></svg></div>

  <div class="card__photo photo--sofa" style="left:93px;top:1996px;width:493px;height:313px" role="img" aria-label="Photo of a sofa beneath a wide garden-view window"></div>
  <div class="card__tag tag--green" style="left:93px;top:2218px;width:316px">Lorem ipsum</div>
  <p class="card__text" style="left:88px;top:2318px">Lorem ipsum dolor sit amet, consectetur adipiscing elit. Quisque vel metus nec massa efficitur pulvinar. Integer rutrum diam quis lectus accumsan.</p>
  <div class="card__link" style="left:84px;top:2433px">Lorem ipsum <svg width="22" height="28" viewBox="0 0 22 28"><path d="M4 3 L16 14 L4 25" fill="none" stroke="#65c81e" stroke-width="7"/></svg></div>

  <div class="card__photo photo--street" style="left:640px;top:1996px;width:490px;height:313px" role="img" aria-label="Photo of a two-storey grey house with a double garage"></div>
  <div class="card__tag tag--dark" style="left:808px;top:2213px;width:320px;text-align:left;padding-left:14px">Lorem ipsum</div>
  <p class="card__text" style="left:640px;top:2318px">Lorem ipsum dolor sit amet, consectetur adipiscing elit. Quisque vel metus nec massa efficitur pulvinar. Integer rutrum diam quis lectus accumsan.</p>
  <div class="card__link" style="left:633px;top:2433px">Lorem ipsum <svg width="22" height="28" viewBox="0 0 22 28"><path d="M4 3 L16 14 L4 25" fill="none" stroke="#65c81e" stroke-width="7"/></svg></div>
</section>

<section>
  <div class="abs contact"></div>
  <h2 class="abs contact__title" style="font-weight:400">Contact us:</h2>
  <div class="abs field" style="left:126px;top:2678px;width:350px;height:45px">lorem ipsum</div>
  <div class="abs field" style="left:500px;top:2678px;width:350px;height:45px">lorem ipsum</div>
  <div class="abs field" style="left:126px;top:2760px;width:350px;height:45px">lorem ipsum</div>
  <div class="abs field" style="left:500px;top:2760px;width:350px;height:45px">lorem ipsum</div>
  <div class="abs textarea"></div>
  <div class="abs btn" style="left:577px;top:3091px;width:273px;height:45px;font-size:22px;padding-left:18px">Lorem ipsum</div>
</section>

<footer>
  <div class="abs footer"></div>
  <div class="abs footer__social">Chatterbook - Snapgram -Chirper</div>
  <p class="abs footer__text">Lorem ipsum dolor sit amet, consectetur adipiscing elit. Quisque vel metus nec massa efficitur pulvinar. Integer rutrum diam quis lectus accumsan, quis consequat neque faucibus.</p>
</footer>

</body>
</html>
```